Business card design and logo for plumbing bussiness

We are wanting a logo for a plumbing business is Queensland Australia. KLV Plumbing and Drainage will be doing works on domestic and commercial sites.
Plumbing, drainage and gas works. We are wanting something that will stand out and be noticed. Colours could be black blue and white but open for suggestions.

Target Market(s)

Builders and home renovators

Industry/Entity Type

Plumbing

Contact Information for Business Card

Dorian Machell - Director
0417 582 031
dorian@klvplumbing-example.com.au
QBCC: 374 8106
ABN: 52 913 207 615

Font styles to use
Sans Serif

Colors
000000

Requirements
Must have
• Clear defined branding

```html
<!DOCTYPE html>
<html lang="en">
<head>
<meta charset="utf-8">
<title>KLV Plumbing and Drainage – Business Card</title>
<link rel="stylesheet" href="https://fonts.googleapis.com/css2?family=Open+Sans:wght@400;600;800&display=swap">
<style>
  :root {
    --page-bg: #e6e6e4;
    --card-bg: #f7f7f5;
    --ink-navy: #1d3a4c;
    --brand-blue: #2f74b3;
    --accent-orange: #f7941d;
    --rule-grey: #8a8f93;
    --card-shadow: rgba(0, 0, 0, 0.14);
  }
  * { box-sizing: border-box; margin: 0; padding: 0; }
  html, body {
    width: 1200px;
    height: 873px;
    overflow: hidden;
    background: var(--page-bg);
    font-family: "Open Sans", Arial, sans-serif;
  }
  .card-sheet {
    position: relative;
    width: 1200px;
    height: 873px;
    display: flex;
    align-items: center;
    justify-content: center;
    gap: 64px;
  }
  .business-card {
    width: 500px;
    height: 300px;
    background: var(--card-bg);
    box-shadow: 0 10px 28px var(--card-shadow);
    display: flex;
    flex-direction: column;
    align-items: center;
    justify-content: center;
  }
  .brand-lockup {
    display: flex;
    flex-direction: column;
    align-items: center;
  }
  .brand-row {
    display: flex;
    align-items: center;
    gap: 12px;
  }
  .brand-dot {
    width: 30px;
    height: 30px;
    border-radius: 50%;
    background: var(--brand-blue);
  }
  .brand-name {
    font-weight: 800;
    color: var(--ink-navy);
    letter-spacing: 0.04em;
    text-transform: uppercase;
  }
  .brand-services {
    margin-top: 6px;
    font-size: 8px;
    letter-spacing: 0.06em;
    color: var(--ink-navy);
    text-transform: uppercase;
  }
  /* contact side */
  .card-contact { justify-content: flex-start; padding-top: 38px; }
  .card-contact .brand-name { font-size: 26px; }
  .card-contact .brand-dot { width: 24px; height: 24px; }
  .card-divider {
    width: 300px;
    height: 1px;
    background: var(--rule-grey);
    margin: 22px 0 18px;
  }
  .contact-block {
    width: 300px;
    font-size: 15px;
    line-height: 1.32;
    color: var(--ink-navy);
  }
  .contact-name {
    color: var(--accent-orange);
    text-transform: uppercase;
    font-weight: 400;
  }
  /* logo side */
  .card-front .brand-name { font-size: 36px; }
  .card-front .brand-dot { width: 38px; height: 38px; }
  .card-front .brand-services { font-size: 10px; margin-top: 8px; }
</style>
</head>
<body>
  <main class="card-sheet">
    <section class="business-card card-contact" aria-label="Business card, contact side">
      <div class="brand-lockup">
        <div class="brand-row">
          <span class="brand-name">KLV Plumbing</span>
          <span class="brand-dot"></span>
        </div>
        <p class="brand-services">Plumbing &nbsp;|&nbsp; Drainage &nbsp;|&nbsp; Gas Works</p>
      </div>
      <div class="card-divider"></div>
      <div class="contact-block">
        <p class="contact-name">Dorian Machell - Director</p>
        <p class="contact-phone">0417 582 031</p>
        <p class="contact-email">dorian@klvplumbing-example.com.au</p>
        <p class="contact-licence">QBCC: 374 8106</p>
        <p class="contact-abn">ABN: 52 913 207 615</p>
      </div>
    </section>

    <section class="business-card card-front" aria-label="Business card, brand side">
      <div class="brand-lockup">
        <div class="brand-row">
          <span class="brand-name">KLV Plumbing</span>
          <span class="brand-dot"></span>
        </div>
        <p class="brand-services">Plumbing &nbsp;|&nbsp; Drainage &nbsp;|&nbsp; Gas Works</p>
      </div>
    </section>
  </main>
</body>
</html>
```